Refresh of Business Card Design

Want to refresh the business card design with the new logo while adhering to style guide as attached. Would like to match feel of website www.durmackvinex.com

```html
<!DOCTYPE html>
<html lang="en">
<head>
<meta charset="utf-8">
<title>Durmack Vinex – Business Card</title>
<link rel="stylesheet" href="https://fonts.googleapis.com/css2?family=Didact+Gothic&family=Poppins:wght@600&display=swap">
<style>
  :root {
    --backdrop: #e6e6ea;
    --card-black: #060607;
    --brand-red: #e8183f;
    --glow-red: #d4163c;
    --text-white: #f4f4f4;
    --silver: #c9cacc;
  }
  * { box-sizing: border-box; margin: 0; padding: 0; }
  html, body { width: 1200px; height: 1200px; overflow: hidden; }
  body {
    background: var(--backdrop);
    font-family: "Didact Gothic", "Century Gothic", sans-serif;
    color: var(--text-white);
    position: relative;
  }
  .card {
    position: absolute;
    left: 179px;
    width: 842px;
    height: 493px;
    background: var(--card-black);
    overflow: hidden;
    box-shadow: 0 1px 3px rgba(0,0,0,0.12);
  }
  .card--front {
    top: 82px;
    background:
      radial-gradient(ellipse 340px 260px at 100% 0%, rgba(212,22,60,0.95) 0%, rgba(120,14,36,0.55) 35%, rgba(6,6,7,0) 75%),
      var(--card-black);
  }
  .card--back {
    top: 624px;
    background:
      radial-gradient(ellipse 320px 250px at 100% 0%, rgba(212,22,60,0.95) 0%, rgba(120,14,36,0.5) 35%, rgba(6,6,7,0) 75%),
      radial-gradient(ellipse 300px 230px at 0% 100%, rgba(212,22,60,0.95) 0%, rgba(120,14,36,0.5) 35%, rgba(6,6,7,0) 75%),
      var(--card-black);
  }

  .name-bar {
    position: absolute;
    left: -30px;
    top: 73px;
    width: 463px;
    height: 50px;
    border: 3px solid var(--silver);
    border-radius: 0 25px 25px 0;
    background: linear-gradient(180deg, #1b1b1d, #050506);
    display: flex;
    align-items: center;
    padding-left: 83px;
  }
  .company-name {
    font-size: 30px;
    letter-spacing: 1.5px;
    color: var(--text-white);
    white-space: nowrap;
    line-height: 1;
  }

  .person { position: absolute; left: 55px; top: 178px; }
  .person__name {
    font-family: "Poppins", "Century Gothic", sans-serif;
    font-weight: 600;
    font-size: 36px;
    color: var(--brand-red);
    line-height: 1.1;
  }
  .person__role { font-size: 20px; margin-top: 0; line-height: 1.2; }

  .contact-list {
    position: absolute;
    left: 55px;
    top: 288px;
    list-style: none;
    font-size: 21px;
    line-height: 32.5px;
  }
  .contact-list li { display: flex; align-items: center; }
  .contact-list .icon { width: 14px; height: 14px; margin: 0 13px 0 4px; flex: none; fill: var(--brand-red); }
  .contact-list .indent { padding-left: 31px; }

  .mark {
    position: absolute;
    left: 536px;
    top: 126px;
    width: 240px;
    height: 240px;
    display: flex;
    flex-direction: column;
    align-items: center;
    justify-content: center;
    gap: 18px;
  }
  .mark__dot { width: 120px; height: 120px; border-radius: 50%; background: var(--brand-red); }
  .mark .company-name { font-size: 24px; }

  .back-bar {
    position: absolute;
    left: 195px;
    top: 226px;
    width: 452px;
    height: 51px;
    border: 3px solid var(--silver);
    border-radius: 26px;
    background: linear-gradient(180deg, #1b1b1d, #050506);
    display: flex;
    align-items: center;
    justify-content: center;
  }
  .back-bar .company-name { font-size: 36px; letter-spacing: 1px; }
</style>
</head>
<body>

<section class="card card--front" aria-label="Business card front">
  <div class="name-bar"><span class="company-name">DURMACK VINEX</span></div>

  <div class="person">
    <h1 class="person__name">Corey Lindell</h1>
    <p class="person__role">Sales</p>
  </div>

  <ul class="contact-list">
    <li>
      <svg class="icon" viewBox="0 0 16 16" aria-hidden="true"><path d="M3.6 1.2l2.3 2.6-1.3 1.9c.9 2 2.6 3.7 4.6 4.6l1.9-1.3 2.6 2.3-1.4 2.4C7.2 13.6 2.4 8.8 1.2 3z"/></svg>
      806.555.0142
    </li>
    <li>
      <svg class="icon" viewBox="0 0 16 16" aria-hidden="true"><path d="M1 3h14v10H1z M1.5 3.5L8 8.5l6.5-5" stroke="#060607" stroke-width="1.2"/></svg>
      clindell@durmackvinex.com
    </li>
    <li>
      <svg class="icon" viewBox="0 0 16 16" aria-hidden="true"><circle cx="8" cy="8" r="7"/><path d="M1 8h14M8 1c-3 3.5-3 10.5 0 14M8 1c3 3.5 3 10.5 0 14" stroke="#060607" stroke-width="1.1" fill="none"/></svg>
      www.durmackvinex.com
    </li>
    <li>
      <svg class="icon" viewBox="0 0 16 16" aria-hidden="true"><path d="M8 0.8a5 5 0 0 1 5 5c0 3.8-5 9.6-5 9.6S3 9.6 3 5.8a5 5 0 0 1 5-5zm0 3a2 2 0 1 0 0 4 2 2 0 0 0 0-4z"/></svg>
      P.O. Box 40213 Harlow, TX 79720
    </li>
    <li class="indent">245 Ridgeway Dr Caston, Texas 79104</li>
  </ul>

  <div class="mark">
    <span class="mark__dot"></span>
    <span class="company-name">DURMACK VINEX</span>
  </div>
</section>

<section class="card card--back" aria-label="Business card back">
  <div class="back-bar"><span class="company-name">DURMACK VINEX</span></div>
</section>

</body>
</html>
```